redesign corporate website (software courses)

We need a complete redesign of the current website: http://q-o-r.biz/ (training: http://q-o-r.biz/pt-br/treinamento/web ); more clear, different color, navigation, header, footer, whatever (side note: site will be based on bootstrap and drupal). Most important pages:

http://q-o-r.biz/pt-br/treinamento (trainingoverviewpage)
http://q-o-r.biz/ (frontpage)
http://q-o-r.biz/pt-br/treinamento/web (trianingdetailpage)

The design should be valid for further content pages (like http://q-o-r.biz/pt-br/desenvolvimentodesoftware) and pages with forms (http://q-o-r.biz/pt-br/contact or http://q-o-r.biz/pt-br/training/web/register)

Logo attached in white and black and black with shadow.

Some other examples of training sites (just content examples - not as template for similar layout):

http://www.brivatutor.example/packages/4817/Website-Development-Professional-training.html?advid=31&gclid=XQa93pLmw42HGtrk5BsjEZWKpR
http://www.code-lehrhaus.example/
http://www.devalto.example/cursos/kestrel-framework-ii/
http://www.varnholt-academy.example/lp/php-development-training.aspx?gclid=MT3hwqUvb52DJYRR8Bpexk9B7B

Industry/Entity Type

Software

```html
<!DOCTYPE html>
<html lang="en">
<head>
<meta charset="utf-8">
<title>Quality Orbit Reskilling</title>
<link rel="stylesheet" href="https://fonts.googleapis.com/css2?family=Catamaran:wght@300;400;500&family=Open+Sans:wght@400;600&display=swap">
<style>
:root{
  --black:#000;
  --white:#fff;
  --orange:#f26522;
  --orange-top:#f7ab35;
  --accent:#f46a1f;
  --text:#7a7a7a;
  --heading:#333;
  --line:#d9d9d9;
  --badge:#c9ccd1;
  --footer-link:#e6e6e6;
}
*{margin:0;padding:0;box-sizing:border-box}
html,body{width:918px;height:1200px;overflow:hidden;background:var(--white)}
body{position:relative;font-family:"Open Sans",sans-serif;color:var(--text)}
.abs{position:absolute}
.site-header{position:absolute;left:0;top:0;width:918px;height:86px;background:var(--black)}
.brand{position:absolute;left:120px;top:26px;display:flex;align-items:center;gap:8px;color:var(--white);font-family:"Catamaran",sans-serif;font-weight:500}
.brand-mark{width:34px;height:34px;border-radius:50%;background:var(--orange)}
.brand-name{font-size:30px;line-height:1}
.brand-tag{font-size:10px;line-height:10px;width:80px;text-transform:uppercase;letter-spacing:.5px}
.main-nav{position:absolute;top:37px;left:0;font-family:"Catamaran",sans-serif;font-size:12.5px;color:var(--white)}
.main-nav span{position:absolute;white-space:nowrap}
.search-icon{position:absolute;left:782px;top:36px}
.hero{position:absolute;left:0;top:86px;width:918px;height:362px;background:linear-gradient(180deg,var(--orange-top),var(--orange))}
.hero-title{position:absolute;left:118px;top:92px;font-family:"Catamaran",sans-serif;font-weight:400;font-size:28px;line-height:31px;color:var(--white)}
.hero-sub{position:absolute;left:118px;top:165px;font-family:"Catamaran",sans-serif;font-size:15.5px;color:var(--white)}
.hero-text{position:absolute;left:118px;top:188px;width:320px;font-size:8.6px;line-height:14.5px;color:var(--white)}
.dots{position:absolute;left:117px;top:230px;display:flex;gap:3px}
.dots i{width:11px;height:11px;border-radius:50%;background:rgba(255,255,255,.45)}
.dots i:first-child{background:var(--white)}
.video-frame{position:absolute;left:474px;top:60px;width:334px;height:224px;background:#f3f3f3;padding:7px}
.video-art{width:100%;height:100%;background:linear-gradient(135deg,#f4f6ef,#e6efe2 45%,#dceef3);display:flex;align-items:center;justify-content:center}
.features{position:absolute;left:64px;top:448px;width:792px;height:134px;background:linear-gradient(180deg,#fff,#f1f1f1)}
.feature{position:absolute;top:479px}
.feature h3{font-family:"Catamaran",sans-serif;font-weight:400;font-size:16px;line-height:18px;color:var(--heading)}
.feature p{font-size:8.6px;line-height:14px;margin-top:3px;padding-left:2px}
.feature a{display:block;margin-top:3px;padding-left:2px;font-size:8.6px;color:var(--accent);text-decoration:none;font-weight:600}
.welcome{position:absolute;left:122px;top:633px;width:452px}
.welcome h2{font-family:"Catamaran",sans-serif;font-weight:400;font-size:19px;color:var(--heading);margin-bottom:6px}
.welcome .lead{font-size:10px;line-height:15px;margin-left:3px;margin-bottom:6px}
.welcome p{font-size:8.4px;line-height:14.4px;margin-left:3px;margin-bottom:6.5px}
.courses{position:absolute;left:596px;top:622px;width:212px;height:226px;border:1px solid var(--line);background:var(--white)}
.courses h4{height:37px;border-bottom:1px solid var(--line);padding:10px 0 0 23px;font-family:"Catamaran",sans-serif;font-weight:400;font-size:14.5px;color:#555;background:#fafafa}
.courses ul{list-style:none;padding:12px 0 0 24px}
.courses li{font-size:9px;line-height:22.2px;color:#666;display:flex;align-items:center;gap:6px}
.partners .badge{position:absolute;top:892px;height:18px;border-radius:3px;background:var(--badge)}
.site-footer{position:absolute;left:0;top:944px;width:918px;height:256px;background:var(--black)}
.foot-col{position:absolute;top:28px}
.foot-col h5{font-family:"Catamaran",sans-serif;font-weight:400;font-size:16px;color:var(--white);margin-bottom:6px}
.foot-col li{list-style:none;font-size:10px;line-height:19px;color:var(--footer-link)}
.social{display:flex;gap:3px;margin-top:2px}
.social i{width:21px;height:21px;border-radius:50%;background:var(--white)}
.foot-rule{position:absolute;left:116px;top:200px;width:692px;height:1px;background:#1f1f1f}
.copyright{position:absolute;left:127px;top:219px;font-size:9px;color:#8a8a8a}
</style>
</head>
<body>
<header class="site-header">
  <div class="brand"><span class="brand-mark"></span><span class="brand-name">QOR</span><span class="brand-tag">Quality Orbit Reskilling</span></div>
  <nav class="main-nav">
    <span style="left:414px">HOME</span>
    <span style="left:472px">TREINAMENTO</span>
    <span style="left:574px">SERVICE</span>
    <span style="left:644px">CAREER</span>
    <span style="left:710px">CONTACT</span>
  </nav>
  <svg class="search-icon" width="16" height="16" viewBox="0 0 16 16"><circle cx="9" cy="7" r="5" fill="none" stroke="#fff" stroke-width="1.8"/><line x1="5.5" y1="10.5" x2="1.5" y2="14.5" stroke="#fff" stroke-width="2"/></svg>
</header>

<section class="hero">
  <svg class="abs" style="left:52px;top:152px" width="20" height="32" viewBox="0 0 20 32"><polyline points="16,3 4,16 16,29" fill="none" stroke="#fff" stroke-width="4"/></svg>
  <svg class="abs" style="left:862px;top:152px" width="20" height="32" viewBox="0 0 20 32"><polyline points="4,3 16,16 4,29" fill="none" stroke="#fff" stroke-width="4"/></svg>
  <h1 class="hero-title">We Provide<br>Software Engineering</h1>
  <div class="hero-sub">Mauris vel lacus vitae felis vestibulum</div>
  <p class="hero-text">Vivamus porttitor g purus nisi eleifend libero a tempus libero lectus feugiat felis Morbi diam mauris viverra in gravida eu mattis in ante</p>
  <div class="dots"><i></i><i></i><i></i><i></i></div>
  <div class="video-frame">
    <div class="video-art" role="img" aria-label="Word cloud around software engineering terms, video preview">
      <svg width="34" height="34" viewBox="0 0 34 34"><circle cx="17" cy="17" r="17" fill="#222"/><polygon points="13,10 25,17 13,24" fill="#fff"/></svg>
    </div>
  </div>
</section>

<section class="features">
</section>
<div class="feature" style="left:114px;top:480px">
  <svg width="40" height="40" viewBox="0 0 40 40"><circle cx="20" cy="20" r="13" fill="#8a8a8a"/><circle cx="20" cy="20" r="5" fill="#fff"/><circle cx="33" cy="7" r="5" fill="none" stroke="#9a9a9a" stroke-width="2"/></svg>
</div>
<div class="feature" style="left:160px"><h3>Treinamento</h3><p>Vivamus porttitor p.urus nisi<br>eleifend libero tempus</p><a href="#">READ MORE</a></div>
<div class="feature" style="left:292px;top:478px">
  <svg width="46" height="38" viewBox="0 0 46 38"><rect x="6" y="4" width="34" height="24" rx="2" fill="none" stroke="#999" stroke-width="1.6"/><path d="M2 30h42l-3 4H5z" fill="#aaa"/><text x="23" y="21" font-size="11" text-anchor="middle" fill="#999" font-family="sans-serif">&lt;/&gt;</text></svg>
</div>
<div class="feature" style="left:346px"><h3>Software<br>Development</h3><p>Vivamus porttitor p.urus nisi</p><a href="#">READ MORE</a></div>
<div class="feature" style="left:470px;top:480px">
  <svg width="42" height="36" viewBox="0 0 42 36"><ellipse cx="21" cy="16" rx="20" ry="15" fill="#8a8a8a"/><path d="M8 26l-3 9 11-6z" fill="#8a8a8a"/><circle cx="12" cy="16" r="3" fill="#fff"/><circle cx="21" cy="16" r="3" fill="#fff"/><circle cx="30" cy="16" r="3" fill="#fff"/></svg>
</div>
<div class="feature" style="left:518px"><h3>Consulting</h3><p>Vivamus porttitor p.urus nisi<br>eleifend libero tempus</p><a href="#">READ MORE</a></div>
<div class="feature" style="left:646px;top:476px">
  <svg width="44" height="42" viewBox="0 0 44 42"><rect x="2" y="6" width="40" height="26" rx="2" fill="none" stroke="#8a8a8a" stroke-width="3"/><rect x="19" y="32" width="6" height="6" fill="#8a8a8a"/><rect x="12" y="38" width="20" height="3" fill="#8a8a8a"/><line x1="22" y1="22" x2="34" y2="2" stroke="#8a8a8a" stroke-width="3"/></svg>
</div>
<div class="feature" style="left:698px"><h3>Web Course</h3><p>Vivamus porttitor p.urus nisi<br>eleifend libero tempus</p><a href="#">READ MORE</a></div>

<section class="welcome">
  <h2>Welcome to Quality Orbit Reskilling</h2>
  <p class="lead">Phasellus felis dolor scelerisque a tempus eget lobortis id libero Donec scelerisque leo ac risus Praesent sit amet est In dictum dolor eu dictum porttitor enim</p>
  <p>felis viverra mi eget luctus massa purus quis odio Etiam nulla massa pharetra facilisis volutpat in imperdiet sit amet sem .Aliquam nec erat at purus cursus interdum Vestibulum ligula augue bibendum accumsan vestibulum ut commodo a mi Morbi ornare gravida elit Integer congue augue et malesuada</p>
  <p>Aculis ipsum dui aliquet felis at cursus magna nisl nec elit Praesent elementum elit at tellus nec ultricies sit amet porttitor mattis enim In massa libero interdum nec interdum vel blandit sed nulla In ullamcorper est eget tempor cursus neque mi consectetuer mi a ultricies massa est sed nisl</p>
  <p>Donec scelerisque leo ac risus Praesent sit amet est In dictum dolor eu dictum porttitor enim felis viverra mi eget luctus massa purus quis odio Etiam nulla massa pharetra facilisis volutpat</p>
</section>

<aside class="courses">
  <h4>OUR COURSES</h4>
  <ul>
    <li><svg width="10" height="9" viewBox="0 0 10 9"><polyline points="1,5 4,8 9,1" fill="none" stroke="#f46a1f" stroke-width="2"/></svg>Morbi ornare gravida elit Integer</li>
    <li><svg width="10" height="9" viewBox="0 0 10 9"><polyline points="1,5 4,8 9,1" fill="none" stroke="#f46a1f" stroke-width="2"/></svg>Congue augue et malesuada</li>
    <li><svg width="10" height="9" viewBox="0 0 10 9"><polyline points="1,5 4,8 9,1" fill="none" stroke="#f46a1f" stroke-width="2"/></svg>Aculis ipsum dui aliquet felis</li>
    <li><svg width="10" height="9" viewBox="0 0 10 9"><polyline points="1,5 4,8 9,1" fill="none" stroke="#f46a1f" stroke-width="2"/></svg>At cursus magna nisl nec elit</li>
    <li><svg width="10" height="9" viewBox="0 0 10 9"><polyline points="1,5 4,8 9,1" fill="none" stroke="#f46a1f" stroke-width="2"/></svg>Praesent elementum elit at</li>
    <li><svg width="10" height="9" viewBox="0 0 10 9"><polyline points="1,5 4,8 9,1" fill="none" stroke="#f46a1f" stroke-width="2"/></svg>Tellus nec ultricies</li>
    <li><svg width="10" height="9" viewBox="0 0 10 9"><polyline points="1,5 4,8 9,1" fill="none" stroke="#f46a1f" stroke-width="2"/></svg>Morbi diam mauris viverra gravida</li>
  </ul>
</aside>

<section class="partners">
  <div class="badge" style="left:132px;width:130px"></div>
  <div class="badge" style="left:286px;width:132px"></div>
  <div class="badge" style="left:444px;width:80px"></div>
  <div class="badge" style="left:552px;width:100px"></div>
  <div class="badge" style="left:678px;width:122px"></div>
</section>

<footer class="site-footer">
  <div class="foot-col" style="left:126px"><h5>Company</h5><ul><li>Why We Are</li><li>How we teach</li><li>About Us</li><li>Consulting</li></ul></div>
  <div class="foot-col" style="left:254px"><h5>Courses</h5><ul><li>Donec scelerisque</li><li>Leo ac risus</li><li>Praesent sit amet</li><li>Dictum dolor</li></ul></div>
  <div class="foot-col" style="left:388px"><h5>Support</h5><ul><li>Support</li><li>Recent Blog</li><li>Testimonials</li></ul></div>
  <div class="foot-col" style="left:519px"><h5>Services</h5><ul><li>Donec scelerisque</li><li>Praesent sit</li><li>Amet est dictum</li><li>Dolor eu dictum</li></ul></div>
  <div class="foot-col" style="left:653px"><h5>Get in touch</h5><div class="social"><i></i><i></i><i></i><i></i></div></div>
  <div class="foot-rule"></div>
  <div class="copyright">© 2014 Company Name &nbsp;All right reserved &nbsp;Term of Use</div>
</footer>
</body>
</html>
```